The most modern business card ever !!!

Our company call “Vantilo”. Vantilo is a technology company specialized in cruises solutions. Out main product is a platform to reserve cruises. This is a revolutionary platform that make easier to travel agencies and final users to reserve cruises across dozen companies like tarvik, welbi, dpv, hbt, etc..We are a “start up”, with a young team of developers and we want to transmit it.. For it, we want something different, a modern business card that represent cruises and technology.. When someone receive this card, this person should say: wowww this is different… this is modern… this is a cruise related company..
Contact Information for Business Card
Requirements
Must have
- diferent, modern
Should not have
- traditions business card

```html
<!DOCTYPE html>
<html lang="en">
<head>
<meta charset="utf-8">
<title>Vantilo Business Card</title>
<link href="https://fonts.googleapis.com/css2?family=Exo+2:wght@500;700&family=Arimo:wght@400&display=swap" rel="stylesheet">
<style>
  :root {
    --backdrop: #1b1b1c;
    --card-top: #3a3a3c;
    --card-bottom: #1f1f21;
    --card-edge: #0e0e0f;
    --logo-ink: #141415;
    --text-light: #f2f2f2;
    --accent-blue: #5b8fd6;
  }
  * { margin: 0; padding: 0; box-sizing: border-box; }
  html, body {
    width: 1200px;
    height: 804px;
    overflow: hidden;
    background: var(--backdrop);
  }
  .canvas {
    position: relative;
    width: 1200px;
    height: 804px;
    display: flex;
    align-items: center;
    justify-content: center;
    gap: 40px;
  }
  .card {
    position: relative;
    width: 525px;
    height: 300px;
    border-radius: 22px;
    background: linear-gradient(160deg, var(--card-top) 0%, #2a2a2c 45%, var(--card-bottom) 100%);
    box-shadow: 0 0 0 1px var(--card-edge);
    display: flex;
    flex-direction: column;
    align-items: center;
    overflow: hidden;
  }
  .brand-name {
    font-family: "Exo 2", sans-serif;
    font-weight: 500;
    color: var(--logo-ink);
    letter-spacing: 2px;
    line-height: 1;
  }
  .card-front .brand-name {
    font-size: 78px;
    margin-top: 38px;
  }
  .holder-name {
    font-family: "Exo 2", sans-serif;
    font-weight: 700;
    font-size: 19px;
    letter-spacing: 1.5px;
    color: var(--text-light);
    margin-top: 22px;
  }
  .holder-role {
    font-family: "Exo 2", sans-serif;
    font-weight: 500;
    font-size: 13px;
    letter-spacing: 1.5px;
    color: var(--accent-blue);
    margin-top: 2px;
  }
  .contact-lines {
    margin-top: 12px;
    font-family: "Arimo", sans-serif;
    font-size: 13px;
    line-height: 1.5;
    color: var(--text-light);
    text-align: center;
  }
  .card-back { justify-content: center; }
  .card-back .brand-name {
    font-size: 92px;
    margin-top: 20px;
  }
  .card-back .web-address {
    font-family: "Arimo", sans-serif;
    font-size: 13px;
    color: var(--text-light);
    margin-top: 34px;
  }
</style>
</head>
<body>
  <main class="canvas">
    <section class="card card-front">
      <div class="brand-name">Vantilo</div>
      <div class="holder-name">MARCUS DELANE</div>
      <div class="holder-role">CEO/FOUNDER</div>
      <div class="contact-lines">
        <p>P: +1 555-014-2287&nbsp;&nbsp;F: +1 555-014-2287&nbsp;&nbsp;E: marcus@vantilo.com</p>
        <p>1840 Harbor Lane, Seaside Point, CA 90412, USA</p>
        <p>www.vantilo.com</p>
      </div>
    </section>
    <section class="card card-back">
      <div class="brand-name">Vantilo</div>
      <div class="web-address">www.vantilo.com</div>
    </section>
  </main>
</body>
</html>
```